Quarveling stickers design for our main topics (for example: agile and Kanban)

We are looking for sticker design, that will reflect our cooperate identity and can be used for the different topics in our company. We would like to start with our Agile Coaching Offers with a Kanban Sticker saying "stop starting, start finishing", A bad example can be find in the file upload ;)
Check out our homepage to get a feeling for the cooperate identity (www.quarveling.ch)

Target Market(s)

Customers and trainees from our trainings

Industry/Entity Type

Consulting

Colors
0355a3
fbed22

Requirements
Must have
• a cool design thats fits to our customer design
the 2 lines can be changed for future stickers ... like in the example "stop starting, start finishing" and "we show you how"
Nice to have
• -
Should not have
• -

```html
<!DOCTYPE html>
<html lang="en">
<head>
<meta charset="utf-8">
<title>Quarveling sticker – stop starting, start finishing</title>
<link rel="stylesheet" href="https://fonts.googleapis.com/css2?family=Fira+Sans:wght@400;600&display=swap">
<style>
  :root {
    --brand-blue: #0355a3;
    --brand-yellow: #fbed22;
    --paper: #ffffff;
  }
  html, body {
    margin: 0;
    padding: 0;
    overflow: hidden;
    background: var(--paper);
  }
  .sticker {
    position: relative;
    width: 1200px;
    height: 368px;
    overflow: hidden;
    background: var(--paper);
    font-family: "Fira Sans", Arial, sans-serif;
  }
  .headline-band {
    position: absolute;
    left: 0;
    top: 0;
    width: 1200px;
    height: 201px;
    background: var(--brand-blue);
  }
  .accent-rule {
    position: absolute;
    left: 0;
    top: 201px;
    width: 1200px;
    height: 10px;
    background: var(--brand-yellow);
  }
  .headline {
    position: absolute;
    left: 56px;
    top: 52px;
    margin: 0;
    font-size: 84px;
    font-weight: 600;
    line-height: 1;
    letter-spacing: 0.2px;
    color: var(--brand-yellow);
    white-space: nowrap;
  }
  .tagline {
    position: absolute;
    left: 56px;
    top: 250px;
    margin: 0;
    font-size: 70px;
    font-weight: 600;
    line-height: 1;
    color: var(--brand-blue);
    white-space: nowrap;
  }
  .brand {
    position: absolute;
    left: 790px;
    top: 232px;
    display: flex;
    align-items: center;
    gap: 22px;
  }
  .brand-square {
    display: block;
    width: 84px;
    height: 84px;
  }
  .brand-name {
    font-size: 46px;
    font-weight: 400;
    line-height: 1;
    color: var(--brand-blue);
    white-space: nowrap;
  }
</style>
</head>
<body>
  <div class="sticker">
    <div class="headline-band"></div>
    <div class="accent-rule"></div>
    <h1 class="headline">stop starting, start finishing</h1>
    <p class="tagline">we show you how</p>
    <div class="brand">
      <svg class="brand-square" viewBox="0 0 84 84" aria-hidden="true">
        <rect x="0" y="0" width="84" height="84" fill="#0355a3"/>
      </svg>
      <span class="brand-name">Quarveling</span>
    </div>
  </div>
</body>
</html>
```